Consulting, Investors, Joint Venture Website

Founded in April 2018, Marendo Consultants Limited (MCL) is an advisory consulting firm specializing in engaging investors in business ventures in Tanzania.
With extensive experience in construction, energy, oil and gas and the legal professions, our team assembles our expertise that allows foreign investors to set foot and flourish in the Tanzanian market.
MCL is locally owned, founded and registered. Our shareholders are cultured Tanzanian citizens with extensive corporate experience in South Africa, Tanzania, United Kingdom and the United States.

Our mission is to provide responsive and unrivalled professional advice from learned and experienced professionals versed in the local market, with an understanding of the cultural and logistical challenges faced by foreign investors.

Our vision is to provide a complete investor’s package that initiates with company registration, compliance and documentation services and ultimately operational facilitation services.

Target Market(s)

Foreign Investors, International companies

Industry/Entity Type

Business Consultant

Number of Pages Required

5+ page

Requirements
Must have
• It will be 5 pages - Home, About Us, Services, Portfolio, Contact Us
Nice to have
• if it can look like https://www.plorvex.example/
• or https://www.dunetri.example or http://www.quillbrook.example/

```html
<!DOCTYPE html>
<html lang="en">
<head>
<meta charset="utf-8">
<title>Marendo Consultants – The Marketing Group</title>
<link href="https://fonts.googleapis.com/css2?family=Raleway:wght@300;400;500;600;700;800;900&display=swap" rel="stylesheet">
<style>
  :root {
    --crimson: #d81b54;
    --navy: #1d1f5c;
    --ink: #454545;
    --muted: #8a8a8a;
    --nav-grey: #666;
    --blush: #fdf7f8;
    --lavender: #e6e8fb;
    --white: #ffffff;
    --footer: #4a4a4a;
    --footer-base: #3b3b3b;
    --footer-text: #b5b5b5;
    --hero-deep: #1c1a7a;
    --hero-mid: #4d44d6;
    --hero-light: #7f77f2;
  }
  * { box-sizing: border-box; margin: 0; padding: 0; }
  html, body { width: 731px; height: 1200px; overflow: hidden; }
  body {
    position: relative;
    font-family: "Raleway", Arial, sans-serif;
    background: var(--white);
    color: var(--ink);
  }
  .site-header {
    position: absolute; left: 0; top: 0; width: 731px; height: 39px;
    background: var(--white);
  }
  .brand {
    position: absolute; left: 61px; top: 7px;
    display: flex; align-items: center; gap: 8px;
    font-size: 18px; font-weight: 500; color: var(--navy);
  }
  .brand-dot {
    width: 25px; height: 25px; border-radius: 50%;
    background: var(--crimson);
  }
  .main-nav a {
    position: absolute; top: 12px; font-size: 13px;
    color: var(--nav-grey); text-decoration: none; font-weight: 400;
  }
  .main-nav a.is-current { color: var(--navy); font-weight: 500; }

  .hero {
    position: absolute; left: 0; top: 39px; width: 731px; height: 372px;
    background:
      radial-gradient(ellipse at 50% 55%, rgba(127,119,242,0.55), transparent 60%),
      linear-gradient(180deg, var(--hero-light) 0%, var(--hero-mid) 40%, var(--hero-deep) 100%);
    text-align: center; color: var(--white);
  }
  .hero-title {
    position: absolute; left: 0; right: 0; top: 112px;
    font-size: 52px; font-weight: 800; letter-spacing: -0.5px;
    text-shadow: 0 2px 6px rgba(0,0,0,0.45);
  }
  .hero-subtitle {
    position: absolute; left: 0; right: 0; top: 172px;
    font-size: 21px; font-weight: 500;
    text-shadow: 0 1px 4px rgba(0,0,0,0.4);
  }
  .hero-cta {
    position: absolute; left: 316px; top: 202px; width: 100px; height: 24px;
    background: var(--crimson); color: var(--white);
    font-size: 15px; font-weight: 500; line-height: 24px;
  }
  .hero-scroll { position: absolute; left: 348px; top: 318px; }

  .section-tab {
    position: absolute; height: 25px; background: var(--crimson);
    color: var(--white); font-size: 15px; font-weight: 500;
    text-align: center; line-height: 25px;
  }
  .section-heading {
    position: absolute; left: 0; right: 0; text-align: center;
    font-size: 18px; font-weight: 700; color: var(--ink);
  }

  .process {
    position: absolute; left: 0; top: 411px; width: 731px; height: 151px;
    background: var(--blush);
  }
  .process-step {
    position: absolute; top: 67px; width: 120px; text-align: center;
  }
  .process-step h3 { font-size: 15px; font-weight: 400; color: var(--ink); }
  .process-step p {
    margin-top: 5px; font-size: 8.5px; line-height: 10.8px; color: var(--muted);
  }
  .process-line {
    position: absolute; top: 78px; height: 2px; background: var(--ink);
  }

  .team {
    position: absolute; left: 0; top: 562px; width: 731px; height: 242px;
    background: var(--lavender);
  }
  .member, .case { position: absolute; text-align: center; }
  .member { top: 64px; width: 140px; }
  .member-photo {
    width: 117px; height: 117px; border-radius: 50%; margin: 0 auto;
    background: linear-gradient(160deg, #c9c4bf, #6f6560);
  }
  .member h3, .case h3 { margin-top: 10px; font-size: 12.5px; font-weight: 500; color: #333; }
  .member p, .case p { font-size: 9px; color: #555; margin-top: 1px; }

  .cases {
    position: absolute; left: 0; top: 804px; width: 731px; height: 254px;
    background: var(--white);
  }
  .case { top: 74px; width: 150px; }
  .case-photo {
    width: 123px; height: 123px; margin: 0 auto;
    background: linear-gradient(150deg, #e9e6df, #9a958c);
  }
  .case h3 { margin-top: 12px; }

  .site-footer {
    position: absolute; left: 0; top: 1058px; width: 731px; height: 105px;
    background: var(--footer); color: var(--white); text-align: center;
  }
  .footer-title { position: absolute; left: 0; right: 0; top: 24px; font-size: 18.5px; font-weight: 700; }
  .footer-cta {
    position: absolute; left: 0; right: 0; top: 50px;
    font-size: 8.5px; color: var(--white); text-decoration: underline;
  }
  .footer-nav {
    position: absolute; left: 61px; width: 608px; top: 72px;
    display: flex; justify-content: space-between; align-items: center;
    font-size: 12.5px; font-weight: 500;
  }
  .footer-nav span.sep { width: 5px; height: 5px; border-radius: 50%; background: var(--white); }
  .footer-base {
    position: absolute; left: 0; top: 1163px; width: 731px; height: 37px;
    background: var(--footer-base); color: var(--footer-text); font-size: 11.5px;
  }
  .copyright { position: absolute; left: 61px; top: 11px; }
  .social { position: absolute; left: 503px; top: 11px; display: flex; align-items: center; gap: 12px; }
  .social .dot { width: 14px; height: 14px; border-radius: 50%; background: var(--white); }
  .social .label { margin-right: 4px; }
</style>
</head>
<body>
  <header class="site-header">
    <div class="brand"><span class="brand-dot"></span>Marendo Consultants</div>
    <nav class="main-nav">
      <a class="is-current" style="left:404px">Home</a>
      <a style="left:477px">About</a>
      <a style="left:543px">Services</a>
      <a style="left:623px">Contact</a>
    </nav>
  </header>

  <section class="hero" role="img" aria-label="Photo of two consultants meeting in a lounge booth, tinted blue-violet">
    <h1 class="hero-title">The Marketing Group</h1>
    <p class="hero-subtitle">Foreign Investors, International Companies</p>
    <div class="hero-cta">Get Started</div>
    <svg class="hero-scroll" width="34" height="24" viewBox="0 0 34 24" aria-hidden="true">
      <path d="M1 3 L17 11 L33 3" fill="none" stroke="#fff" stroke-width="3"/>
      <path d="M1 13 L17 21 L33 13" fill="none" stroke="#fff" stroke-width="4"/>
    </svg>
  </section>

  <section class="process">
    <div class="section-tab" style="left:275px;top:0;width:182px">Read about the</div>
    <h2 class="section-heading" style="top:38px">PROCESS</h2>
    <div class="process-step" style="left:92px"><h3>Idea</h3><p>Lorem Ipsum is simply dummy text of the printing and type setting industry.</p></div>
    <span class="process-line" style="left:194px;width:117px"></span>
    <div class="process-step" style="left:305px"><h3>Planning</h3><p>Lorem Ipsum is simply dummy text of the printing and type setting industry.</p></div>
    <span class="process-line" style="left:419px;width:118px"></span>
    <div class="process-step" style="left:520px"><h3>Success</h3><p>Lorem Ipsum is simply dummy text of the printing and type setting industry.</p></div>
  </section>

  <section class="team">
    <h2 class="section-heading" style="top:26px">OUR TEAM</h2>
    <div class="member" style="left:54px"><div class="member-photo" role="img" aria-label="Portrait of the managing director"></div><h3>Lorem Ipsum</h3><p>Managing Director</p></div>
    <div class="member" style="left:212px"><div class="member-photo" role="img" aria-label="Portrait of the strategic head"></div><h3>Lorem Ipsum</h3><p>Strategic Head</p></div>
    <div class="member" style="left:370px"><div class="member-photo" role="img" aria-label="Portrait of the support provider"></div><h3>Lorem Ipsum</h3><p>Support Peovider</p></div>
    <div class="member" style="left:536px"><div class="member-photo" role="img" aria-label="Portrait of the technical lead"></div><h3>Lorem Ipsum</h3><p>Technical Banda</p></div>
  </section>

  <section class="cases">
    <div class="section-tab" style="left:316px;top:0;width:100px">Read Our</div>
    <h2 class="section-heading" style="top:37px">CASE STUDIES</h2>
    <div class="case" style="left:48px"><div class="case-photo" role="img" aria-label="Hand writing figures in a notebook"></div><h3>Lorem Ipsum</h3><p>Market Resurch #2</p></div>
    <div class="case" style="left:207px"><div class="case-photo" role="img" aria-label="Calculator on handwritten strategy notes"></div><h3>Lorem Ipsum</h3><p>Market Growth</p></div>
    <div class="case" style="left:365px"><div class="case-photo" role="img" aria-label="Close-up of a financial ledger sheet"></div><h3>Lorem Ipsum</h3><p>Technology in Business</p></div>
    <div class="case" style="left:532px"><div class="case-photo" role="img" aria-label="Computer mouse, cup and pen on a newspaper"></div><h3>Lorem Ipsum</h3><p>Right Timing</p></div>
  </section>

  <footer class="site-footer">
    <h2 class="footer-title">Feel Free To Communicate</h2>
    <a class="footer-cta">Book an Appointment!</a>
    <nav class="footer-nav">
      <span>Home</span><span class="sep"></span>
      <span>About</span><span class="sep"></span>
      <span>Services</span><span class="sep"></span>
      <span>Case Studies</span><span class="sep"></span>
      <span>Our Team</span><span class="sep"></span>
      <span>Process</span><span class="sep"></span>
      <span>Contact</span>
    </nav>
  </footer>
  <div class="footer-base">
    <p class="copyright">2020 copyright by the business group</p>
    <div class="social"><span class="label">Follow us on</span><span class="dot"></span><span class="dot"></span><span class="dot"></span></div>
  </div>
</body>
</html>
```